Business card - mobile service

O KiraTel is a mobile family safety service based on tablets and smartphones.
The business card must have:
BASIC INFO
Company Logo
Name
Position / Job Title: Co-founder
Mobile Phone Number: +55 (11) 5080 6172
Land Line: +55 (11) 9087 614352
Email Address: name@kiratel-example.com
Web Site URL: www.kiratel-example.com
PROMOTIONAL INFO
Try KiraTel free Today!
Your personal promo code: xxxx-2222-uuuu-7777-1234
Promo code text explanation with the instructions about the trial offer
Updates
Dears,
One more must have: the KiraTel slogan:
Industry/Entity Type
Safety
Look and feel
Each slider illustrates characteristics of the customer's brand and the style your logo design should communicate.

```html
<!DOCTYPE html>
<html lang="en">
<head>
<meta charset="utf-8">
<title>KiraTel business card</title>
<link rel="stylesheet" href="https://fonts.googleapis.com/css2?family=Open+Sans:wght@400;600;700;800&display=swap">
<style>
  :root {
    --stage: #ececec;
    --blue: #1a8dc6;
    --blue-deep: #0c6fa9;
    --blue-light: #8fd0ea;
    --brand-blue: #1c9ccf;
    --yellow: #f7c21a;
    --orange: #f7941d;
    --white: #ffffff;
    --ink: #6b6b6b;
  }
  * { margin: 0; padding: 0; box-sizing: border-box; }
  html, body { width: 1200px; height: 900px; overflow: hidden; background: var(--stage); font-family: "Open Sans", sans-serif; }
  .card {
    position: absolute; left: 279px; width: 525px; height: 300px;
    border-radius: 20px; overflow: hidden;
    box-shadow: 0 3px 6px rgba(0,0,0,.45);
  }
  .card-front { top: 85px; background: radial-gradient(circle at 85% 60%, #3fb0dc 0%, var(--blue) 45%, var(--blue-deep) 100%); }
  .card-back { top: 413px; background: linear-gradient(180deg, #ffffff 0%, #f1f1f1 100%); }

  .wordmark { position: absolute; display: flex; align-items: center; gap: 8px; font-weight: 800; letter-spacing: -0.5px; }
  .card-front .wordmark { left: 31px; top: 36px; font-size: 34px; color: var(--white); }
  .card-back .wordmark { left: 270px; top: 96px; font-size: 44px; color: var(--brand-blue); }
  .wordmark-dot { width: .6em; height: .6em; border-radius: 50%; background: var(--yellow); }

  .promo { position: absolute; left: 130px; top: 175px; color: var(--white); font-size: 15px; line-height: 22px; }
  .promo-code { font-size: 17px; }
  .promo-note { margin-top: 14px; font-size: 14.5px; line-height: 21px; }

  .badge {
    position: absolute; left: 398px; top: 140px; width: 122px; height: 122px; border-radius: 50%;
    background: radial-gradient(circle at 40% 35%, #ffb03a 0%, var(--orange) 70%);
    box-shadow: 2px 3px 5px rgba(0,0,0,.3);
    color: var(--white); transform: rotate(18deg); text-align: center;
  }
  .badge-lead { display: block; margin-top: 22px; font-size: 13.5px; }
  .badge-free { display: block; font-size: 30px; font-weight: 800; line-height: 34px; }

  .person { position: absolute; left: 37px; top: 46px; }
  .person-name { font-size: 19px; font-weight: 700; color: var(--brand-blue); }
  .person-role { font-size: 14px; color: var(--ink); margin-top: 1px; }

  .contacts { position: absolute; left: 44px; top: 127px; list-style: none; }
  .contacts::before { content: ""; position: absolute; left: 23px; top: 0; width: 2px; height: 76px; background: var(--yellow); }
  .contacts li { display: flex; align-items: center; height: 19px; font-size: 12.5px; color: var(--ink); }
  .contacts svg { width: 11px; height: 11px; margin-right: 25px; fill: var(--brand-blue); }

  .wave { position: absolute; left: 0; top: 0; }
  .slogan { position: absolute; left: 307px; top: 266px; font-size: 14.5px; color: var(--white); }
  .slogan em { font-style: normal; color: var(--blue-light); }
</style>
</head>
<body>
  <section class="card card-front">
    <div class="wordmark">KiraTel<span class="wordmark-dot"></span></div>
    <div class="promo">
      <p>Your personal promo</p>
      <p>code: <span class="promo-code">xxxx-2222-uuuu-7777-1234</span></p>
      <p class="promo-note">Promo code text explanation with<br>the instructions about the trial offer</p>
    </div>
    <div class="badge"><span class="badge-lead">Try it today for</span><span class="badge-free">FREE</span></div>
  </section>

  <section class="card card-back">
    <svg class="wave" width="525" height="300" viewBox="0 0 525 300">
      <defs>
        <linearGradient id="waveFill" x1="0" y1="0" x2="1" y2="0">
          <stop offset="0" stop-color="#2a5f9c"/>
          <stop offset="0.5" stop-color="#1f7fbd"/>
          <stop offset="1" stop-color="#38b4dc"/>
        </linearGradient>
      </defs>
      <path d="M0 226 C 90 250, 170 230, 250 190 C 340 150, 440 165, 525 205 L525 190 C 440 150, 340 140, 250 178 C 170 212, 90 236, 0 218 Z" fill="#a9dcef"/>
      <path d="M0 232 C 90 262, 180 240, 260 200 C 350 160, 450 172, 525 215 L525 300 L0 300 Z" fill="url(#waveFill)"/>
    </svg>
    <div class="person">
      <p class="person-name">Marcus Halloway</p>
      <p class="person-role">Co-founder</p>
    </div>
    <ul class="contacts">
      <li><svg viewBox="0 0 12 12"><path d="M1 4 Q6 0 11 4 L9 6 L7.5 5 L4.5 5 L3 6 Z M3 7 H9 V11 H3 Z"/></svg>+55 (11) 5080 6172</li>
      <li><svg viewBox="0 0 12 12"><rect x="1" y="8" width="2" height="3"/><rect x="4" y="6" width="2" height="5"/><rect x="7" y="4" width="2" height="7"/><rect x="10" y="2" width="2" height="9"/></svg>+55 (11) 9087 614352</li>
      <li><svg viewBox="0 0 12 12"><path d="M1 3 H11 V10 H1 Z M1.8 3.6 L6 7 L10.2 3.6 L10.2 4.6 L6 8 L1.8 4.6 Z" fill-rule="evenodd"/></svg>name@kiratel-example.com</li>
      <li><svg viewBox="0 0 12 12"><circle cx="6" cy="6" r="5"/><rect x="2" y="5.3" width="8" height="1.4" fill="#fff"/></svg>www.kiratel-example.com</li>
    </ul>
    <div class="wordmark">KiraTel<span class="wordmark-dot"></span></div>
    <p class="slogan">Your <em>Family Safety</em> Service</p>
  </section>
</body>
</html>
```